Yoga for Scoliosis business card/logo design

I need a business card/logo design for my new business. I am a registered yoga teacher and am certified in yoga for scoliosis. I'd like my card to read "Marlow Yoga Yoga for a Healthy Spine" and would like to incorporate one of the letters in my name{ ie the first vertical line of the letter " H "or "D"} to resemble a scoliotic spine. I regularly teach the following:Yoga for Scoliosis, Yoga for Back Health, Hatha yoga, Vinyasa yoga with Iyengar style alignment. This business is mostly for private clients, but I also teach group, semi-private & work shop classes. I like the colors green (light emerald) and royal blue. I'd like the design to be somewhat sleek, but not too modern. I also like the idea of a ying/yang symbol with a scoliotic spine dviding it.

Danielle Marlow
200 RYT, Certified Yoga for Scoliosis Instructor
MarlowYoga.example
MarlowYoga@mailbox.example
555-412-3097

```html
<!DOCTYPE html>
<html lang="en">
<head>
<meta charset="utf-8">
<title>Marlow Yoga for a Healthy Spine – Business Cards</title>
<link rel="stylesheet" href="https://fonts.googleapis.com/css2?family=Damion&family=Arimo:wght@400;700&display=swap">
<style>
  :root {
    --page-bg: #ffffff;
    --teal-top: #175e68;
    --teal-mid: #12505a;
    --teal-deep: #0f3a40;
    --teal-darkest: #0c2d31;
    --silver-light: #f4f5f6;
    --silver-mid: #b9bdc1;
    --silver-dark: #7d8388;
    --navy-top: #2a1d4e;
    --navy-mid: #1b3f72;
    --ocean: #1a6a8c;
    --ocean-deep: #17557a;
    --gold-light: #fff3a6;
    --gold-mid: #f1c33b;
    --gold-dark: #b77a12;
  }
  * { box-sizing: border-box; margin: 0; padding: 0; }
  html, body { width: 1062px; height: 1200px; overflow: hidden; background: var(--page-bg); }
  .canvas { position: relative; width: 1062px; height: 1200px; }

  .card { position: absolute; overflow: hidden; }
  .card--silver { left: 27px; top: 27px; width: 1008px; height: 563px; background: var(--teal-top); }
  .card--gold { left: 30px; top: 612px; width: 1005px; height: 566px;
    background: linear-gradient(180deg, var(--navy-top) 0%, var(--navy-mid) 45%, var(--ocean-deep) 100%); }

  .card__waves, .card__title { position: absolute; inset: 0; width: 100%; height: 100%; }
  .card__title text { font-family: "Damion", cursive; }

  .contact-list { position: absolute; left: 36px; list-style: none; font-family: "Arimo", sans-serif; font-size: 29px; white-space: nowrap; }
  .card--silver .contact-list { top: 217px; color: var(--silver-light); }
  .card--gold .contact-list { top: 148px; color: var(--gold-mid); }
  .contact-list li { display: flex; align-items: center; height: 65px; }
  .contact-list .icon { width: 28px; height: 28px; margin-right: 22px; flex: none; }
  .contact-list .icon-at { width: 28px; margin-right: 22px; text-align: center; font-size: 27px; }
  .card--silver .icon { fill: var(--silver-mid); stroke: var(--silver-mid); }
  .card--gold .icon { fill: var(--gold-mid); stroke: var(--gold-mid); }

  .brand-badge {
    position: absolute; width: 264px; height: 264px; border-radius: 50%;
    display: flex; align-items: center; justify-content: center;
    font-family: "Damion", cursive; font-size: 48px; text-align: center; line-height: 1;
  }
  .card--silver .brand-badge { left: 716px; top: 279px; border: 8px solid var(--silver-mid); color: var(--silver-light); }
  .card--gold .brand-badge { left: 713px; top: 291px; border: 8px solid var(--gold-dark); color: var(--gold-mid); }
</style>
</head>
<body>
<div class="canvas">

  <section class="card card--silver">
    <svg class="card__waves" viewBox="0 0 1008 563" preserveAspectRatio="none" aria-hidden="true">
      <path d="M0,395 C260,360 470,440 680,420 C820,405 930,330 1008,325 L1008,563 L0,563 Z" fill="var(--teal-mid)"/>
      <path d="M0,440 C280,400 520,470 720,470 C860,470 950,420 1008,400 L1008,563 L0,563 Z" fill="var(--teal-deep)"/>
      <path d="M0,520 C300,500 600,540 1008,500 L1008,563 L0,563 Z" fill="var(--teal-darkest)"/>
    </svg>
    <svg class="card__title" viewBox="0 0 1008 563" role="heading" aria-level="1">
      <defs>
        <linearGradient id="silver-ink" x1="0" y1="0" x2="0" y2="1">
          <stop offset="0" stop-color="#f4f5f6"/>
          <stop offset="0.5" stop-color="#b9bdc1"/>
          <stop offset="0.72" stop-color="#7d8388"/>
          <stop offset="1" stop-color="#f4f5f6"/>
        </linearGradient>
      </defs>
      <text x="63" y="140" font-size="100" textLength="908" lengthAdjust="spacingAndGlyphs" fill="url(#silver-ink)">Marlow Yoga for a Healthy Spine</text>
    </svg>
    <ul class="contact-list">
      <li><svg class="icon" viewBox="0 0 30 30"><circle cx="15" cy="9" r="7" stroke="none"/><path d="M2,29 C2,19 28,19 28,29 Z" stroke="none"/></svg>Danielle Marlow 200 RYT, Certified Yoga for Scoliosis Instructor</li>
      <li><svg class="icon" viewBox="0 0 30 30"><rect x="8" y="1" width="14" height="28" rx="3" fill="none" stroke-width="2.5"/></svg>555-412-3097</li>
      <li><span class="icon-at">@</span>MarlowYoga@mailbox.example</li>
      <li><svg class="icon" viewBox="0 0 30 30"><circle cx="15" cy="15" r="13" stroke="none"/><path d="M2,15 H28 M15,2 V28 M6,7 H24 M6,23 H24" fill="none" stroke="var(--teal-deep)" stroke-width="1.5"/></svg>MarlowYoga.example</li>
    </ul>
    <div class="brand-badge">Marlow<br>Yoga</div>
  </section>

  <section class="card card--gold">
    <svg class="card__waves" viewBox="0 0 1005 566" preserveAspectRatio="none" aria-hidden="true">
      <path d="M0,425 C250,385 520,440 720,420 C850,405 940,340 1005,330 L1005,566 L0,566 Z" fill="var(--ocean)" opacity="0.75"/>
      <path d="M0,470 C300,440 560,500 760,490 C880,485 960,450 1005,440 L1005,566 L0,566 Z" fill="var(--ocean-deep)"/>
    </svg>
    <svg class="card__title" viewBox="0 0 1005 566" role="heading" aria-level="1">
      <defs>
        <linearGradient id="gold-ink" x1="0" y1="0" x2="0" y2="1">
          <stop offset="0" stop-color="#fff3a6"/>
          <stop offset="0.45" stop-color="#f1c33b"/>
          <stop offset="0.75" stop-color="#b77a12"/>
          <stop offset="1" stop-color="#fff3a6"/>
        </linearGradient>
      </defs>
      <text x="138" y="118" font-size="82" textLength="774" lengthAdjust="spacingAndGlyphs" fill="url(#gold-ink)">Marlow Yoga for a Healthy Spine</text>
    </svg>
    <ul class="contact-list">
      <li><svg class="icon" viewBox="0 0 30 30"><circle cx="15" cy="9" r="7" stroke="none"/><path d="M2,29 C2,19 28,19 28,29 Z" stroke="none"/></svg>Danielle Marlow 200 RYT, Certified Yoga for Scoliosis Instructor</li>
      <li><svg class="icon" viewBox="0 0 30 30"><rect x="8" y="1" width="14" height="28" rx="3" fill="none" stroke-width="2.5"/></svg>555-412-3097</li>
      <li><span class="icon-at">@</span>MarlowYoga@mailbox.example</li>
      <li><svg class="icon" viewBox="0 0 30 30"><circle cx="15" cy="15" r="13" stroke="none"/><path d="M2,15 H28 M15,2 V28 M6,7 H24 M6,23 H24" fill="none" stroke="var(--navy-mid)" stroke-width="1.5"/></svg>MarlowYoga.example</li>
    </ul>
    <div class="brand-badge">Marlow<br>Yoga</div>
  </section>

</div>
</body>
</html>
```